KOVER Wealth Partners Brochure
Brochure Design 2011
Your Objectives Through Independence
We need a tri-fold brochure for our company KOVER Wealth Partners. We already have a custom logo created and need that inserted into the brochure. We are a independent financial services company, we offer investment advice and products to consumers and business.
Financial Services
Consumers & Business
Must use our current company logo,you can get it here:
https://photoshelf-example.net/MarcusLindt/KOVERWealthPartners?authkey=Xq7TmLbNZr2Wd9YkHfPe&feat=directlink
Also need all content including sections to be editable. Need at least three sections (Example: "The Company", "Our Services", etc...)
KOVER Wealth Partners Logo
Logo AI file
Logo AI File 2.0
Old Brochure Cover (Prime Ledger)
old brochure Inner (Prime Ledger)
This is a brochure which I like the style, simple and clean
Another Brochure in which I like
by far my favorite one, hope this inspires some ideas
more ideas

```html
<!DOCTYPE html>
<html lang="en">
<head>
<meta charset="utf-8">
<title>KOVER Wealth Partners – Tri-fold Brochure</title>
<link rel="stylesheet" href="https://fonts.googleapis.com/css2?family=Raleway:wght@300;400;600;700&display=swap">
<style>
  :root {
    --page-bg: #e9eaec;
    --paper: #f3f4f5;
    --charcoal: #41474a;
    --olive: #7c911f;
    --ink: #3b3f42;
    --faint: #d3d6d8;
    --muted: #8a8f92;
    --white: #ffffff;
  }
  * { margin: 0; padding: 0; box-sizing: border-box; }
  html, body {
    width: 1200px; height: 901px; overflow: hidden;
    background: var(--page-bg);
    font-family: "Raleway", Arial, sans-serif;
    color: var(--ink);
  }
  .brochure {
    position: absolute; left: 40px; top: 18px;
    width: 1120px; height: 866px;
    display: flex;
    background: var(--paper);
    box-shadow: 0 4px 18px rgba(0,0,0,.12);
  }
  .panel {
    position: relative; width: 373.33px; height: 100%;
    overflow: hidden;
    border-right: 1px solid #e1e3e5;
  }
  .panel:last-child { border-right: none; }

  /* Left panel – testimonials */
  .photo {
    position: absolute; left: 0; top: 0; width: 100%; height: 210px;
    background: linear-gradient(135deg, #2c2f33 0%, #5a5f63 45%, #c9c6c0 75%, #e8e5df 100%);
  }
  .quote-box {
    position: absolute; left: 0; top: 330px; width: 270px; height: 150px;
    background: var(--olive); color: var(--white);
    padding: 18px 22px;
  }
  .quote-mark { font-size: 64px; font-weight: 700; line-height: .8; height: 40px; }
  .quote-text { font-size: 12px; line-height: 1.45; margin-top: 6px; }
  .quote-author { font-size: 11px; font-weight: 600; margin-top: 8px; }
  .side-word {
    position: absolute; right: 34px; top: 240px;
    writing-mode: vertical-rl;
    font-size: 40px; font-weight: 300; letter-spacing: 6px;
    color: var(--faint);
  }
  .left-foot {
    position: absolute; left: 26px; bottom: 40px;
    font-size: 10px; line-height: 1.6; color: var(--muted);
  }

  /* Middle panel – back */
  .contact-band {
    position: absolute; left: 0; top: 0; width: 100%; height: 250px;
    background: var(--charcoal); color: var(--white);
    display: flex; flex-direction: column; align-items: center; justify-content: center;
    text-align: center; gap: 10px;
  }
  .band-tag { font-size: 11px; letter-spacing: 1px; }
  .brand-mark { display: flex; align-items: center; gap: 8px; }
  .brand-square { width: 18px; height: 18px; background: var(--white); }
  .brand-name { font-size: 22px; font-weight: 700; letter-spacing: 3px; }
  .band-sub { font-size: 10px; letter-spacing: 2px; }
  .band-contact { font-size: 10px; line-height: 1.6; }
  .back-foot {
    position: absolute; left: 30px; right: 30px; bottom: 40px;
    display: flex; align-items: flex-end; justify-content: space-between; gap: 14px;
  }
  .disclaimer { font-size: 9px; line-height: 1.5; color: var(--muted); width: 160px; }
  .badges { display: flex; gap: 10px; }
  .badge { width: 24px; height: 24px; background: var(--muted); }

  /* Right panel – cover */
  .cover-title {
    position: absolute; left: 70px; top: 150px;
    font-size: 30px; line-height: 1.1; letter-spacing: 1px;
  }
  .cover-title .lead { font-weight: 300; color: var(--ink); display: block; }
  .cover-title .accent { font-weight: 700; color: var(--olive); display: block; }
  .cover-bar {
    position: absolute; left: 102px; top: 300px; width: 46px; height: 390px;
    background: var(--charcoal);
    display: flex; align-items: center; justify-content: center;
  }
  .cover-bar span {
    writing-mode: vertical-rl;
    color: var(--white); font-size: 13px; letter-spacing: 3px; font-weight: 600;
  }
  .cover-brand {
    position: absolute; left: 80px; top: 712px;
    display: flex; align-items: center; gap: 8px;
  }
  .cover-brand .brand-square { background: var(--charcoal); width: 22px; height: 22px; }
  .cover-brand .brand-name { color: var(--charcoal); font-size: 28px; }
  .cover-echo {
    position: absolute; left: 170px; top: 300px;
    writing-mode: vertical-rl;
    font-size: 44px; font-weight: 300; line-height: 1.05; letter-spacing: 4px;
    color: var(--faint);
  }
  .cover-web {
    position: absolute; right: 26px; bottom: 30px;
    font-size: 10px; color: var(--muted);
  }
</style>
</head>
<body>
  <main class="brochure">
    <section class="panel panel-testimonials">
      <div class="photo" role="img" aria-label="Photo of a hand signing a document at a desk"></div>
      <div class="quote-box">
        <div class="quote-mark">“</div>
        <p class="quote-text">Their independent advice gave our family a clear plan and real confidence in every financial decision we made.</p>
        <p class="quote-author">— Helen R., Client</p>
      </div>
      <h2 class="side-word">TESTIMONIALS</h2>
      <div class="left-foot">
        <p>www.koverwealth.com</p>
        <p>555-014-2288</p>
      </div>
    </section>

    <section class="panel panel-back">
      <div class="contact-band">
        <p class="band-tag">Independent Advice Since 1998</p>
        <div class="brand-mark">
          <span class="brand-square"></span>
          <span class="brand-name">KOVER</span>
        </div>
        <p class="band-sub">INVESTMENT SERVICES</p>
        <p class="band-contact">120 Harbor Lane, Suite 4<br>Phone 555-014-2288</p>
      </div>
      <div class="back-foot">
        <p class="disclaimer">Securities offered through an independent registered broker dealer. Member of regional networks.</p>
        <div class="badges">
          <span class="badge"></span>
          <span class="badge"></span>
          <span class="badge"></span>
        </div>
      </div>
    </section>

    <section class="panel panel-cover">
      <h1 class="cover-title">
        <span class="lead">YOUR</span>
        <span class="lead">OBJECTIVES</span>
        <span class="accent">THROUGH</span>
        <span class="accent">INDEPENDENCE</span>
      </h1>
      <div class="cover-bar"><span>INVESTMENT SERVICES</span></div>
      <div class="cover-brand">
        <span class="brand-square"></span>
        <span class="brand-name">KOVER</span>
      </div>
      <p class="cover-echo" aria-hidden="true">YOUR<br>OBJECTIVES<br>THROUGH<br>INDEPENDENCE</p>
      <p class="cover-web">www.koverwealth.com</p>
    </section>
  </main>
</body>
</html>
```